Modern Design Business Card industrial maintenance company

Business card design for Company named Brookvale Equipment Services

Target Market(s)

Industrial

Industry/Entity Type

Maintenance and repair

Contact Information for Business Card

Place holder for address, office phone, mobile number and email

Requirements
Must have
• Clean modern look
Nice to have
• N/a

```html
<!DOCTYPE html>
<html lang="en">
<head>
<meta charset="utf-8">
<title>Brookvale Equipment Services – Business Card</title>
<link rel="stylesheet" href="https://fonts.googleapis.com/css2?family=Poppins:wght@400;600;700&display=swap">
<style>
  :root {
    --bg: #2a2a2c;
    --card: #1b1c1e;
    --card-back: #141517;
    --ink: #ffffff;
    --rule: #6a6b6e;
    --emboss: #232427;
  }
  * { box-sizing: border-box; margin: 0; padding: 0; }
  html, body { width: 1200px; height: 1108px; overflow: hidden; }
  body {
    background: var(--bg);
    font-family: "Poppins", sans-serif;
    color: var(--ink);
    position: relative;
  }
  .card {
    position: absolute;
    top: 194px;
    width: 440px;
    height: 720px;
    border-radius: 22px;
  }
  .card--front {
    left: 130px;
    background: var(--card);
    display: flex;
    flex-direction: column;
    align-items: center;
    padding-top: 78px;
    text-align: center;
  }
  .card--back {
    left: 630px;
    background: var(--card-back);
    overflow: hidden;
  }
  .brand-mark {
    width: 104px; height: 104px;
    border: 5px solid var(--ink);
    border-radius: 50%;
  }
  .brand-name {
    margin-top: 18px;
    font-weight: 600;
    font-size: 46px;
    line-height: 1;
    letter-spacing: 2px;
    text-transform: uppercase;
  }
  .brand-tagline {
    margin-top: 6px;
    font-weight: 600;
    font-size: 15px;
    letter-spacing: 6.5px;
    text-transform: uppercase;
  }
  .person-name {
    margin-top: 52px;
    font-weight: 700;
    font-size: 28px;
    letter-spacing: 0.5px;
    text-transform: uppercase;
  }
  .person-title {
    font-weight: 400;
    font-size: 17px;
    letter-spacing: 0.5px;
    text-transform: uppercase;
    line-height: 1.1;
  }
  .icon-row {
    margin-top: 20px;
    width: 300px;
    display: flex;
    align-items: center;
    gap: 10px;
  }
  .icon-row::before, .icon-row::after {
    content: ""; flex: 1; height: 1px; background: var(--rule);
  }
  .icon {
    width: 30px; height: 30px;
    background: var(--ink);
    border-radius: 5px;
    display: flex; align-items: center; justify-content: center;
  }
  .icon svg { width: 20px; height: 20px; }
  .contact-list {
    margin-top: 12px;
    list-style: none;
    font-size: 19px;
    line-height: 1.45;
  }
  .rule {
    width: 300px; height: 1px;
    background: var(--rule);
    margin: 14px 0;
  }
  .address { font-size: 19px; line-height: 1.4; font-style: normal; }
  .pattern {
    position: absolute; inset: 0;
    background: linear-gradient(160deg, #1c1d20 0%, var(--card-back) 60%, #101113 100%);
  }
  .back-mark {
    position: absolute;
    left: 250px; top: 560px;
    width: 40px; height: 40px;
    border: 3px solid var(--ink);
    border-radius: 50%;
  }
</style>
</head>
<body>
  <section class="card card--front" aria-label="Business card front">
    <div class="brand-mark"></div>
    <h1 class="brand-name">Brookvale</h1>
    <p class="brand-tagline">Equipment Services</p>

    <h2 class="person-name">Daniel Harper</h2>
    <p class="person-title">Managing Director</p>

    <div class="icon-row">
      <span class="icon" aria-label="Phone">
        <svg viewBox="0 0 24 24"><path fill="#1b1c1e" d="M6.6 10.8a15.1 15.1 0 0 0 6.6 6.6l2.2-2.2c.3-.3.7-.4 1-.2 1.1.4 2.3.6 3.6.6.6 0 1 .4 1 1V20c0 .6-.4 1-1 1A17 17 0 0 1 3 4c0-.6.4-1 1-1h3.5c.6 0 1 .4 1 1 0 1.3.2 2.5.6 3.6.1.3 0 .7-.2 1z"/></svg>
      </span>
      <span class="icon" aria-label="Email">
        <svg viewBox="0 0 24 24"><rect x="3" y="5" width="18" height="14" rx="1.5" fill="#1b1c1e"/><path d="M3.5 6l8.5 7 8.5-7" stroke="#fff" stroke-width="1.6" fill="none"/></svg>
      </span>
      <span class="icon" aria-label="Website">
        <svg viewBox="0 0 24 24"><circle cx="12" cy="12" r="9" fill="#1b1c1e"/><path d="M3 12h18M12 3c3 3 3 15 0 18M12 3c-3 3-3 15 0 18" stroke="#fff" stroke-width="1.3" fill="none"/></svg>
      </span>
    </div>

    <ul class="contact-list">
      <li>044-555 210 347</li>
      <li>info@brookvale.com</li>
      <li>www.brookvaleservices.com</li>
    </ul>

    <div class="rule"></div>

    <address class="address">421, Address line goes here<br>45452, Country Name</address>
  </section>

  <section class="card card--back" aria-label="Business card back">
    <div class="pattern" role="img" aria-label="Tonal embossed repeating brand monogram pattern covering the card"></div>
    <div class="back-mark"></div>
  </section>
</body>
</html>
```